Mental Health

QRT HAVEN
Behavioral Health
4172 W. Pell St. Mesa, AZ 85219
Gwendolyn (480)555-0142 / Omar 480-555-0187

Email: QRTHaven@Mailvex.example
Newly Remodeled & Spacious
g Staff
Registered Nurses
Licensed Independent &
Professional Substance &
Abuse Counselors
Behavioral Health Techs
Certified Caregivers
Behavioral Health &
Substance Abuse Professionals

To Refer a Patient
About Us
QRT Haven is a Fully Staffed Behavioral
Health Residential Facility, providing
treatment plans for adults suffering
with various Behavioral Health and
Substance Abuse disorders, while living
in a nice safe, clean and supportive
environment. Our home offers clients the
ability to learn the necessary skills to
help clients adapt, build self confidence
as well as independence, with the goal
of reducing the probability of a future
crisis or possible relapse. We offer
counseling programs, consisting of a
variety of addiction and recovery support
groups, independent living, coping and
social skills groups, as well as assisting
clients with using tools to create a resume
to help obtain employment and so much
more. We are committed to teaching
self management care and allowing
clients to understand how to utilize the
resources, skills and tools available for
long term success by providing superior
quality, all-inclusive living arrangements
and treatment options.

Thank you for your patience while I update the final content needed for us to make the final decision this week.

```html
<!DOCTYPE html>
<html lang="en">
<head>
<meta charset="utf-8">
<title>QRT Haven – Business Card</title>
<link href="https://fonts.googleapis.com/css2?family=Roboto:wght@300;400;700&display=swap" rel="stylesheet">
<style>
  :root {
    --page-bg: #eeeeee;
    --brand-blue: #1f70ad;
    --brand-blue-soft: #2f7cb6;
    --brand-green: #7ab648;
    --ink-dark: #555555;
    --ink-mid: #5f5f5f;
    --white: #ffffff;
  }
  html, body {
    margin: 0;
    padding: 0;
    width: 1200px;
    height: 1000px;
    overflow: hidden;
    background: var(--page-bg);
    font-family: "Roboto", Arial, sans-serif;
  }
  .card {
    position: absolute;
    left: 279px;
    width: 643px;
    height: 385px;
    box-shadow: 0 3px 8px rgba(0,0,0,0.28);
    overflow: hidden;
  }
  .card--front { top: 88px; background: var(--brand-blue); }
  .card--back { top: 527px; background: var(--white); }
  .card-art { position: absolute; left: 0; top: 0; }

  .front-brand {
    position: absolute;
    left: 0; right: 0;
    top: 150px;
    display: flex;
    align-items: center;
    justify-content: center;
    gap: 18px;
  }
  .front-brand__dot {
    width: 86px; height: 86px;
    border-radius: 50%;
    background: var(--white);
  }
  .front-brand__name {
    color: var(--white);
    font-size: 52px;
    font-weight: 400;
    letter-spacing: 1px;
  }

  .back-brand {
    position: absolute;
    left: 46px; top: 47px;
    display: flex;
    align-items: center;
    gap: 10px;
  }
  .back-brand__dot {
    width: 56px; height: 56px;
    border-radius: 50%;
    background: var(--brand-blue);
  }
  .back-brand__name {
    color: var(--brand-blue);
    font-size: 30px;
    font-weight: 400;
  }
  .company-name {
    position: absolute;
    left: 45px; top: 118px;
    margin: 0;
    font-size: 39px;
    font-weight: 700;
    color: var(--ink-dark);
    letter-spacing: 0.3px;
    line-height: 1.2;
  }
  .company-tagline {
    position: absolute;
    left: 46px; top: 163px;
    margin: 0;
    font-size: 22px;
    font-weight: 400;
    color: var(--ink-mid);
    line-height: 1.2;
  }
  .contact-list {
    position: absolute;
    left: 45px; top: 268px;
    margin: 0; padding: 0;
    list-style: none;
  }
  .contact-item {
    display: flex;
    align-items: center;
    gap: 7px;
    height: 24px;
    margin-bottom: 1px;
    font-size: 15.5px;
    font-weight: 300;
    color: var(--ink-mid);
    white-space: nowrap;
  }
  .contact-icon { width: 19px; height: 19px; flex: none; display: block; }
</style>
</head>
<body>

<section class="card card--front">
  <svg class="card-art" width="643" height="385" viewBox="0 0 643 385">
    <rect class="pattern-area" width="643" height="385" fill="var(--brand-blue)"
          role="img" aria-label="Faint pattern of head silhouettes in profile on blue"/>
  </svg>
  <div class="front-brand">
    <span class="front-brand__dot"></span>
    <span class="front-brand__name">QRT Haven</span>
  </div>
</section>

<section class="card card--back">
  <svg class="card-art" width="643" height="385" viewBox="0 0 643 385">
    <defs>
      <linearGradient id="orbGradient" x1="0" y1="0" x2="1" y2="0">
        <stop offset="0" stop-color="#7ab648"/>
        <stop offset="1" stop-color="#2f73ab"/>
      </linearGradient>
    </defs>
    <rect class="pattern-area" width="643" height="385" fill="var(--brand-blue)"
          role="img" aria-label="Faint pattern of head silhouettes in profile on blue"/>
    <path class="swoosh-green" fill="var(--brand-green)"
          d="M0 0 H268 C340 8 392 40 406 78 L372 168 C352 220 344 268 402 276 C490 286 580 288 582 310 C584 330 530 360 492 385 H0 Z"/>
    <path class="white-field" fill="var(--white)"
          d="M0 0 H255 C328 10 378 40 392 76 L358 170 C338 222 330 272 390 280 C470 290 560 290 566 308 C570 326 518 360 478 385 H0 Z"/>
    <circle class="accent-orb" cx="406" cy="123" r="53" fill="url(#orbGradient)"/>
  </svg>

  <div class="back-brand">
    <span class="back-brand__dot"></span>
    <span class="back-brand__name">QRT Haven</span>
  </div>

  <h1 class="company-name">QRT HAVEN</h1>
  <p class="company-tagline">Behavioral Health</p>

  <ul class="contact-list">
    <li class="contact-item">
      <svg class="contact-icon" viewBox="0 0 20 20"><circle cx="10" cy="10" r="10" fill="var(--brand-green)"/><path d="M10 4.5a3.5 3.5 0 0 0-3.5 3.5c0 2.6 3.5 7 3.5 7s3.5-4.4 3.5-7A3.5 3.5 0 0 0 10 4.5z" fill="#fff"/><circle cx="10" cy="8" r="1.3" fill="var(--brand-green)"/></svg>
      <span>4172 W. Pell St. Mesa, AZ 85219</span>
    </li>
    <li class="contact-item">
      <svg class="contact-icon" viewBox="0 0 20 20"><circle cx="10" cy="10" r="10" fill="var(--brand-green)"/><path d="M6.5 5.2l2 .2.8 2.3-1.2 1a6 6 0 0 0 3.2 3.2l1-1.2 2.3.8.2 2c-.4.6-1.2 1-2 .9C9.4 14 6 10.6 5.6 7.2c-.1-.8.3-1.6.9-2z" fill="#fff"/></svg>
      <span>Gwendolyn (480)555-0142 / Omar 480-555-0187</span>
    </li>
    <li class="contact-item">
      <svg class="contact-icon" viewBox="0 0 20 20"><circle cx="10" cy="10" r="10" fill="var(--brand-green)"/><rect x="5" y="6.5" width="10" height="7" rx="0.8" fill="#fff"/><path d="M5.3 7l4.7 3.6L14.7 7" fill="none" stroke="var(--brand-green)" stroke-width="1"/></svg>
      <span>QRTHaven@Mailvex.example</span>
    </li>
  </ul>
</section>

</body>
</html>
```